New Business Card Design Project

Removed as project is complete.

Target Market(s)

Industry/Entity Type

Business

Requirements
Must have
• Removed as project is complete.
Nice to have
Should not have

```html
<!DOCTYPE html>
<html lang="en">
<head>
<meta charset="utf-8">
<title>Lanternway Compliance – Business Card</title>
<link rel="stylesheet" href="https://fonts.googleapis.com/css2?family=Open+Sans:wght@400;600;700&display=swap">
<style>
  :root {
    --stage: #e6e3df;
    --card-light: #ffffff;
    --card-dark: #000000;
    --ink: #1d1d1d;
    --ink-soft: #3a3a3a;
    --brand-orange: #f08a1c;
    --brand-red: #e23a2c;
    --brand-yellow: #f9d21b;
    --divider: #8a8a8a;
    --tagline: #f2f2f2;
  }
  * { box-sizing: border-box; margin: 0; padding: 0; }
  html, body { width: 1200px; height: 900px; overflow: hidden; }
  body {
    background: var(--stage);
    font-family: "Open Sans", Arial, sans-serif;
    color: var(--ink);
    position: relative;
  }
  .card {
    position: absolute;
    top: 274px;
    width: 536px;
    height: 326px;
    overflow: hidden;
  }
  .card--front { left: 56px; background: var(--card-light); }
  .card--back { left: 619px; background: var(--card-dark); }

  .brand {
    display: flex;
    align-items: center;
    gap: 10px;
  }
  .brand__dot {
    width: 22px; height: 22px;
    border-radius: 50%;
    background: var(--brand-orange);
    flex: none;
  }
  .brand__name {
    font-weight: 600;
    color: var(--brand-orange);
    font-size: 24px;
    letter-spacing: -0.2px;
    white-space: nowrap;
  }
  .card--front .brand { position: absolute; left: 22px; top: 62px; }

  .person { position: absolute; left: 34px; top: 180px; font-size: 15px; line-height: 21px; }
  .person__name { font-weight: 700; }
  .person__role, .person__credentials { color: var(--ink-soft); }

  .divider {
    position: absolute; left: 180px; top: 182px;
    width: 1px; height: 64px; background: var(--divider);
  }

  .contacts {
    position: absolute; left: 230px; top: 178px;
    list-style: none; font-size: 16px; line-height: 23px;
  }
  .contacts li { display: flex; align-items: center; gap: 8px; }
  .contacts svg { width: 15px; height: 15px; flex: none; }

  .company-line {
    position: absolute; left: 20px; top: 296px;
    font-size: 10.5px; color: var(--ink);
  }
  .company-line strong { font-weight: 700; }

  .accent-bar {
    position: absolute; left: 0; right: 0; bottom: 0; height: 12px;
    background: linear-gradient(90deg, var(--brand-yellow), var(--brand-orange) 50%, var(--brand-red));
  }

  .card--back .brand {
    position: absolute; left: 0; right: 0; top: 130px; justify-content: center;
  }
  .card--back .brand__name { font-size: 27px; }
  .glow-line {
    position: absolute; left: 150px; width: 240px; top: 198px; height: 1px;
    background: linear-gradient(90deg, transparent, rgba(255,255,255,0.55), transparent);
  }
  .tagline {
    position: absolute; left: 0; right: 0; top: 218px;
    text-align: center; color: var(--tagline); font-size: 19px;
  }
</style>
</head>
<body>
  <section class="card card--front" aria-label="Business card front">
    <div class="brand">
      <span class="brand__dot"></span>
      <span class="brand__name">Lanternway Compliance</span>
    </div>

    <div class="person">
      <div class="person__name">Mark Delaney</div>
      <div class="person__role">Director</div>
      <div class="person__credentials">BBus, CAMS</div>
    </div>

    <div class="divider"></div>

    <ul class="contacts">
      <li>
        <svg viewBox="0 0 16 16" aria-hidden="true"><path d="M3 1h3l1.5 4-2 1.3a9 9 0 0 0 4.2 4.2L11 8.5l4 1.5v3a2 2 0 0 1-2 2A12 12 0 0 1 1 3a2 2 0 0 1 2-2z" fill="var(--brand-red)"/></svg>
        <span>+61 (0)100 200 300</span>
      </li>
      <li>
        <svg viewBox="0 0 16 16" aria-hidden="true"><rect x="1" y="3" width="14" height="10" fill="none" stroke="var(--brand-red)" stroke-width="1.6"/><path d="M1.5 3.5 8 9l6.5-5.5" fill="none" stroke="var(--brand-red)" stroke-width="1.6"/></svg>
        <span>hello@lanternwaycompliance.com</span>
      </li>
      <li>
        <svg viewBox="0 0 16 16" aria-hidden="true"><circle cx="8" cy="8" r="6.5" fill="none" stroke="var(--brand-red)" stroke-width="1.5"/><ellipse cx="8" cy="8" rx="2.8" ry="6.5" fill="none" stroke="var(--brand-red)" stroke-width="1.2"/><path d="M1.5 8h13M3 4.5h10M3 11.5h10" stroke="var(--brand-red)" stroke-width="1.1"/></svg>
        <span>www.lanternwaycompliance.com</span>
      </li>
    </ul>

    <p class="company-line"><strong>Lanternway Compliance International Pty Ltd</strong> | P.O. Box 2210, Ryde Park NSW 2100</p>
    <div class="accent-bar"></div>
  </section>

  <section class="card card--back" aria-label="Business card back">
    <div class="brand">
      <span class="brand__dot"></span>
      <span class="brand__name">Lanternway Compliance</span>
    </div>
    <div class="glow-line"></div>
    <p class="tagline">Guiding every step to compliance...</p>
  </section>
</body>
</html>
```